New Electrical Business Card Design

I would like a new design for my business cards.
i would like the same logo and font but new design
Please see attached files for front and back design.
large image can be used for graphics.
I would like the instagram link incorporated to back of card.
website site address needs to be changed to www.tidemarkelectrical.au
everything else stays as is

```html
<!DOCTYPE html>
<html lang="en">
<head>
<meta charset="utf-8">
<title>Tidemark Electrical &amp; Data – Business Card</title>
<link rel="stylesheet" href="https://fonts.googleapis.com/css2?family=Montserrat:wght@400;700;800&display=swap">
<style>
  :root {
    --page-bg: #1d1d1d;
    --card-dark: #2a2a2a;
    --card-light: #ffffff;
    --brand-green: #0f8a43;
    --brand-grey: #808080;
    --ink: #1c1c1c;
    --ink-soft: #333333;
    --white: #ffffff;
    --disc: #ececec;
  }
  * { box-sizing: border-box; margin: 0; padding: 0; }
  html, body {
    width: 1200px; height: 988px; overflow: hidden;
    background: var(--page-bg);
    font-family: "Montserrat", sans-serif;
  }
  .sheet {
    position: relative; width: 1200px; height: 988px;
    display: flex; flex-direction: column; align-items: center; justify-content: center; gap: 40px;
  }
  .card {
    position: relative; width: 760px; height: 434px;
    border-radius: 28px; overflow: hidden;
  }
  .card--back { background: var(--card-dark); }
  .card--front { background: var(--card-light); }

  /* business name */
  .business-name {
    font-family: "Montserrat", sans-serif; font-weight: 700;
    line-height: 1.2; white-space: nowrap;
  }
  .card--back .business-name {
    position: absolute; left: 0; right: 0; top: 150px;
    text-align: center; font-size: 40px; color: var(--white);
  }
  .card--front .business-name {
    position: absolute; left: 56px; top: 62px;
    font-size: 30px; color: var(--ink);
  }

  .social {
    position: absolute; left: 0; right: 0; top: 296px;
    display: flex; align-items: center; justify-content: center; gap: 12px;
    color: var(--white); font-size: 22px; font-weight: 400; letter-spacing: 0.5px;
  }
  .social__mark {
    width: 20px; height: 20px; border-radius: 5px;
    border: 2px solid var(--brand-green);
  }

  .disc {
    position: absolute; right: 40px; top: 34px;
    width: 280px; height: 280px; border-radius: 50%; background: var(--disc);
  }

  .person {
    position: absolute; left: 56px; top: 140px;
    font-size: 28px; font-weight: 800; letter-spacing: 0.5px; text-transform: uppercase;
  }
  .person__first { color: var(--brand-green); }
  .person__last { color: var(--brand-grey); }

  .registration {
    position: absolute; left: 56px; top: 190px;
    font-size: 17px; line-height: 1.3; color: var(--ink-soft);
  }

  .contacts {
    position: absolute; left: 56px; top: 252px; list-style: none;
    font-size: 17px; line-height: 1.55; color: var(--ink-soft);
  }
  .contacts li { display: flex; align-items: center; gap: 10px; }
  .contacts svg { width: 16px; height: 16px; flex: none; }

  .services {
    position: absolute; left: 56px; bottom: 40px;
    display: flex; align-items: center; gap: 12px;
    font-size: 19px; color: var(--ink-soft); letter-spacing: 0.3px;
  }
  .services__dot { width: 6px; height: 6px; border-radius: 50%; background: var(--brand-green); }
</style>
</head>
<body>
<main class="sheet">

  <section class="card card--back" aria-label="Card back">
    <p class="business-name">Tidemark Electrical &amp; Data</p>
    <p class="social"><span class="social__mark"></span>tidemark.electrical</p>
  </section>

  <section class="card card--front" aria-label="Card front">
    <div class="disc"></div>
    <p class="business-name">Tidemark Electrical &amp; Data</p>
    <p class="person"><span class="person__first">Daniel</span> <span class="person__last">Ostrowski</span></p>
    <p class="registration">ABN - 12 604 887 219<br>Lic Number - 581064B</p>
    <ul class="contacts">
      <li>
        <svg viewBox="0 0 16 16" aria-hidden="true"><path fill="#0f8a43" d="M3.6 1.2l2.3 2.4-1.2 1.8c.9 2 2.4 3.6 4.4 4.6l1.8-1.2 2.4 2.3-1.3 2.4C6.6 13.3 2.6 9.3 1.2 3z"/></svg>
        0400 318 762
      </li>
      <li>
        <svg viewBox="0 0 16 16" aria-hidden="true"><rect x="1" y="3" width="14" height="10" rx="1" fill="#0f8a43"/><path d="M1.5 3.8L8 9l6.5-5.2" fill="none" stroke="#fff" stroke-width="1.3"/></svg>
        info@tidemarkelectrical.au
      </li>
      <li>
        <svg viewBox="0 0 16 16" aria-hidden="true"><circle cx="8" cy="8" r="7" fill="#0f8a43"/><path d="M1 8h14M8 1c-3 3.5-3 10.5 0 14M8 1c3 3.5 3 10.5 0 14" fill="none" stroke="#fff" stroke-width="1"/></svg>
        www.tidemarkelectrical.au
      </li>
    </ul>
    <p class="services">
      Residential <span class="services__dot"></span>
      Commercial <span class="services__dot"></span>
      Industrial <span class="services__dot"></span>
      24hr Service
    </p>
  </section>

</main>
</body>
</html>
```